New theme for existing wordpress site

We have an existing website at www.halvergatecw.com which uses wordpress. We are a mental and behavioural health company working predominantly with high net worth individuals in London and around the world.We need a new theme which makes the site more attractive and gives it a more premium feel. We would like to explore two possible concepts. Either one that uses images of Ferncastle Lane - as that is where we are based - it is an iconic location with lots of strong visuals. Or one which uses portraits of people. People are key to the work we do. Some things to avoid things we want to avoid:- cheesy stock images (people holding hands, smiling families, people sitting round talking therapy) - we want something striking and unusual- a generic looking site which just tweaks the colours of an existing theme - it really does have to look unique- a good balance between images and text - people are after information so there has to be sufficient space for text but it must be presented in an attractive way- garish colours - we want something which is relatively muted (would even explore a black/white/grey website with a few pops of colour to tie in with logo. No orange please.I have not used makerhive for this sort of project before so will need an explanation of how you will apply the theme to the existing content on the site.Feel free to use the HCW logo for colour and font inspiration. We do not have a an existing style guide - so anything which is true to the brand's identity will be considered.Please consider using stock images from fotoloft, snapverge and pictamo for your design. If you want images of Ferncastle Lane these can be supplied.

Target Market(s)

Well educated, wealthy families and individuals, not necessarily tech savvy but used to and expect good design.

Industry/Entity Type

Health And Wellness

Font styles to use
Sans Serif

Colors

Designer to choose colors to be used in the design.

Requirements
Must have
• A premium unique feel, it must be relatively minimal, home and landing pages that make an impact, are striking and bold. Must have strong royalty free imagery. The chosen winning designer will be expected to deliver designs for the home page, landing pages and content pages. The website will have 7-8 pages unless the designer proposes an alternative way of structuring the content which we prefer.
Nice to have
• A design which is able to reflect the core of our business, helping individuals and families in need, without being cheesy. A video landing page could be cool.
• Should be calm, and cool.
• Be good to see a monochrome design with a pop of colour.
Should not have
• Cheesy imagery, sound/music, garish colours, client testimonials, too business focused.

```html
<!DOCTYPE html>
<html lang="en">
<head>
<meta charset="utf-8">
<title>Halvergate Clinical Wellbeing – Team &amp; Contact</title>
<link href="https://fonts.googleapis.com/css2?family=Poppins:wght@300;400;500;600&display=swap" rel="stylesheet">
<style>
:root{
  --white:#ffffff;
  --team-overlay:rgba(95,95,100,0.42);
  --contact-bg:#7f7f7f;
  --field-bg:#999999;
  --footer-bg:#3f3f3f;
  --footer-text:#a5a5a5;
  --accent:#00a8e1;
}
*{margin:0;padding:0;box-sizing:border-box}
html,body{width:1124px;height:1200px;overflow:hidden}
body{font-family:"Poppins",sans-serif;color:var(--white);position:relative;background:var(--contact-bg)}
.team{position:absolute;left:0;top:0;width:1124px;height:566px;overflow:hidden}
.team-backdrop{position:absolute;inset:0;background:linear-gradient(90deg,#c9b878 0%,#bca585 18%,#c99a9a 34%,#9bb7b2 50%,#7fb3c4 62%,#a9b4be 78%,#9fb0bd 100%)}
.team-shade{position:absolute;inset:0;background:var(--team-overlay)}
.section-title{position:absolute;left:155px;font-weight:600;font-size:24px;letter-spacing:.5px}
.team-lead{position:absolute;left:155px;top:102px;width:340px;font-size:17.5px;line-height:20px;font-weight:300}
.team-note{position:absolute;left:591px;top:104px;width:385px;font-size:10px;line-height:11.8px;font-weight:300}
.team-note p+p{margin-top:11px}
.team-note b{font-weight:600}
.member{position:absolute;top:199px;width:146px}
.portrait{width:106px;height:105px;background:linear-gradient(160deg,#d8d8d8,#6c6c6c)}
.portrait.dark{background:linear-gradient(160deg,#555,#1e1e1e)}
.member-name{margin-top:15px;font-size:17px;line-height:19.5px;font-weight:300;white-space:normal}
.member-role{font-size:9.6px;line-height:11px;font-weight:400}
.member-bio{margin-top:13px;font-size:10px;line-height:11.8px;font-weight:300}
.member-bio p+p{margin-top:11.8px}
.contact{position:absolute;left:0;top:566px;width:1124px;height:582px;background:var(--contact-bg);overflow:hidden}
.contact-portrait{position:absolute;left:50px;top:20px;width:470px;height:562px;background:radial-gradient(ellipse at 45% 45%,#5a5a5a 0%,#3e3e3e 45%,rgba(127,127,127,0) 72%)}
.contact-info{position:absolute;left:155px;top:36px;width:365px}
.contact-info .section-title{position:static}
.contact-intro{margin-top:6px;font-size:10px;line-height:12.7px;font-weight:300}
.company{margin-top:16px;font-size:17px;font-weight:300}
.address{margin-top:9px;font-size:11.5px;line-height:14px;font-weight:300}
.contact-line{margin-top:13px;font-size:11.5px;font-weight:300}
.contact-line+.contact-line{margin-top:11px}
.map-button{position:absolute;left:156px;top:335px;width:144px;height:43px;border:2px solid var(--white);display:flex;align-items:center;justify-content:center;font-size:10.5px;font-weight:500;letter-spacing:2.4px}
.enquiry-form{position:absolute;left:591px;top:76px;width:378px}
.field-label{display:block;font-size:11.2px;font-weight:400;height:25px;line-height:17px}
.field{height:35px;background:var(--field-bg);margin-bottom:11px}
.field.message{height:71px}
.submit{margin-top:32px;width:144px;height:43px;background:var(--accent);display:flex;align-items:center;justify-content:center;font-size:10.5px;font-weight:500;letter-spacing:2.4px}
.site-footer{position:absolute;left:0;top:1148px;width:1124px;height:52px;background:var(--footer-bg);display:flex;align-items:center;justify-content:center;font-size:8.5px;color:var(--footer-text)}
</style>
</head>
<body>
<section class="team">
  <div class="team-backdrop" role="img" aria-label="Row of pastel painted terraced houses on Ferncastle Lane"></div>
  <div class="team-shade"></div>
  <h2 class="section-title" style="top:44px">OUR TEAM</h2>
  <p class="team-lead">Anders Lindqvist set up Halvergate Clinical Wellbeing in 2016 with the help of Miles Ashworth-Kerr.</p>
  <div class="team-note">
    <p>Since then the company has grown to become the leading provider of Case Management and Recovery Coaching in Europe. You can find out more about the team below.</p>
    <p>Halvergate Clinical Wellbeing also has a number of coaches – you can find out more about them <b>here.</b></p>
  </div>

  <article class="member" style="left:154px">
    <div class="portrait" role="img" aria-label="Black and white portrait of Anders Lindqvist"></div>
    <h3 class="member-name">Anders Lindqvist</h3>
    <div class="member-role">Founder</div>
    <div class="member-bio">
      <p>Anders has worked in the behavioural health field for 20 years.</p>
      <p>He has worked as a therapist, set up or run treatment facilities in Europe, the USA and the Middle East and currently works with individuals, families and organisations around the world in tailoring solutions which work for each individual case.</p>
    </div>
  </article>

  <article class="member" style="left:323px">
    <div class="portrait" role="img" aria-label="Black and white portrait of Miles Ashworth-Kerr"></div>
    <h3 class="member-name">Miles<br>Ashworth-Kerr</h3>
    <div class="member-role">Director</div>
    <div class="member-bio">
      <p>Miles has a decade of experience of working as a therapist and has worked in both clinical and managerial roles within treatment facilities.</p>
      <p>He undertakes therapy and case management for Halvergate Clinical Wellbeing basing himself in London and Surrey.</p>
    </div>
  </article>

  <article class="member" style="left:490px">
    <div class="portrait dark" role="img" aria-label="Black and white portrait of Helena Marsh"></div>
    <h3 class="member-name">Helena Marsh</h3>
    <div class="member-role">Deputy Director</div>
    <div class="member-bio">
      <p>Helena is one of the country's leading and most experienced case managers and oversees Halvergate Clinical Wellbeing's recovery coaching service.</p>
    </div>
  </article>

  <article class="member" style="left:659px">
    <div class="portrait dark" role="img" aria-label="Black and white portrait of Daniel Whitcombe"></div>
    <h3 class="member-name" style="white-space:nowrap">Daniel Whitcombe</h3>
    <div class="member-role">Case Manager</div>
    <div class="member-bio">
      <p>Daniel is a qualified life coach and is a professional musician. He was previously the Student and Well-being Coach at The Northfield School of Arts and helped found the charity Quaverlight Trust which helps people with addiction and mental health problems in the music industry.</p>
    </div>
  </article>

  <article class="member" style="left:829px">
    <div class="portrait" role="img" aria-label="Black and white portrait of Nikolai Lindqvist by the sea"></div>
    <h3 class="member-name">Nikolai<br>Lindqvist</h3>
    <div class="member-role">Chief Operating Officer</div>
    <div class="member-bio">
      <p>Nikolai has more than 20 years' experience supporting organisations improve their communications, growth and performance.</p>
    </div>
  </article>
</section>

<section class="contact">
  <div class="contact-portrait" role="img" aria-label="Black and white side profile of a laughing man in a hooded top"></div>
  <div class="contact-info">
    <h2 class="section-title">CONTACT</h2>
    <p class="contact-intro">Halvergate Clinical Wellbeing provides tailored, specialist support to individuals and families with behavioural and addiction difficulties. We have offices in London and work with clients across the world. If you want a member of the team to get in touch with you please complete the below form.</p>
    <h3 class="company">Halvergate Clinical Wellbeing</h3>
    <address class="address" style="font-style:normal">17 Ashcombe Terrace<br>Westbourne Green<br>London<br>W10 4QT</address>
    <div class="contact-line">enquiries@halvergatecw.com</div>
    <div class="contact-line">(+44) 020 7946 0182</div>
  </div>
  <div class="map-button">VIEW MAP</div>

  <form class="enquiry-form">
    <span class="field-label">First Name:</span><div class="field"></div>
    <span class="field-label">Last Name:</span><div class="field"></div>
    <span class="field-label">Email:</span><div class="field"></div>
    <span class="field-label">Phone:</span><div class="field"></div>
    <span class="field-label">How can we help?</span><div class="field message"></div>
    <div class="submit">SUBMIT</div>
  </form>
</section>

<footer class="site-footer">© All content of this website is copyright of Halvergate Clinical Wellbeing Ltd</footer>
</body>
</html>
```